Business Card - Rebranding for Consulting Firm

We are renaming and rebranding our consulting firm and need to raise the level of quality of our cards as part of that effort. We consult to leading high tech, life science and other innovation sector companies.

Need a two-sided business card design.

Side 1: (a) Company logo (b) tag line: Optimize Your Investment in Talent (c) Name (d) Title (e) Phone 1: Office (f) Phone 2: Mobile (g) email: person@HollowmereAdvisory.com

Side 2: Two lines of text: (a) Growth is Imperative. Change is Constant. Talent Executes Strategy. (b) We help you excel at all three.

Target Market(s)

Business and human resources executives and senior managers

Industry/Entity Type

Management Consulting

Contact Information for Business Card

Font styles to use
Sans Serif

Requirements
Must have
• clean, not too busy, but with a bit of creativity. Stick to the colors used in the attached logo
• appeal to high tech, life science companies
Nice to have
• prefer white background

```html
<!DOCTYPE html>
<html lang="en">
<head>
<meta charset="utf-8">
<title>Hollowmere Advisory – Business Card</title>
<link href="https://fonts.googleapis.com/css2?family=Montserrat:wght@400;500;600;700&display=swap" rel="stylesheet">
<style>
  :root {
    --backdrop: #1c1d20;
    --brand-dark: #1b5fa0;
    --brand-mid: #1f7cc1;
    --brand-light: #27a6e0;
    --grey-text: #8a9199;
    --card-white: #ffffff;
    --card-grey: #eeeff1;
  }
  * { box-sizing: border-box; margin: 0; padding: 0; }
  html, body { width: 1200px; height: 900px; overflow: hidden; }
  body {
    background: var(--backdrop);
    font-family: "Montserrat", sans-serif;
    display: flex; flex-direction: column; align-items: center; justify-content: center; gap: 40px;
  }
  .card {
    position: relative; width: 700px; height: 400px; border-radius: 26px; overflow: hidden;
  }
  /* Side 2 – statement side */
  .card--statement { background: var(--card-grey); }
  .statement-brand {
    position: absolute; left: 0; right: 0; top: 120px;
    display: flex; align-items: center; justify-content: center; gap: 18px;
  }
  .brand-square { width: 46px; height: 46px; background: var(--brand-light); }
  .brand-name { color: var(--brand-dark); font-weight: 600; line-height: 1; }
  .statement-brand .brand-name { font-size: 52px; letter-spacing: -1px; }
  .statement-brand .brand-name small { display: block; font-size: 15px; letter-spacing: 9px; margin-top: 6px; font-weight: 600; }
  .statement-lines { position: absolute; left: 0; right: 0; bottom: 52px; text-align: center; }
  .statement-line { color: var(--brand-dark); font-size: 17px; font-weight: 500; }
  .statement-cta { color: var(--brand-light); font-size: 17px; font-weight: 500; margin-top: 4px; letter-spacing: .5px; }

  /* Side 1 – contact side */
  .card--contact { background: var(--card-white); }
  .contact-brand {
    position: absolute; left: 60px; top: 110px; width: 200px;
    display: flex; flex-direction: column; align-items: center; gap: 12px; text-align: center;
  }
  .contact-brand .brand-square { width: 70px; height: 70px; }
  .contact-brand .brand-name { font-size: 22px; }
  .divider { position: absolute; left: 290px; top: 80px; width: 1px; height: 170px; background: var(--brand-light); }
  .contact-details { position: absolute; left: 320px; top: 78px; }
  .person-name { color: var(--brand-dark); font-size: 26px; font-weight: 700; letter-spacing: 1px; }
  .person-title { color: var(--brand-light); font-size: 17px; font-weight: 500; margin-top: 2px; }
  .contact-list { list-style: none; margin-top: 14px; }
  .contact-list li { display: flex; align-items: center; gap: 12px; color: var(--brand-dark); font-size: 19px; line-height: 29px; }
  .contact-list svg { width: 14px; height: 14px; flex: none; }
  .tagline-band { position: absolute; left: 0; right: 0; top: 310px; height: 26px; background: var(--brand-mid); }
  .tagline-pill {
    position: absolute; left: 165px; top: 298px; height: 50px; padding: 0 26px;
    background: var(--brand-light); border: 3px solid var(--card-white); border-radius: 12px;
    display: flex; align-items: center;
    color: var(--card-white); font-size: 19px; font-weight: 600; letter-spacing: .5px; text-transform: uppercase;
  }
</style>
</head>
<body>
  <section class="card card--statement" aria-label="Card back">
    <div class="statement-brand">
      <span class="brand-square"></span>
      <span class="brand-name">Hollowmere<small>ADVISORY LLC</small></span>
    </div>
    <div class="statement-lines">
      <p class="statement-line">Growth is Imperative • Change is Constant • Talent Executes Strategy</p>
      <p class="statement-cta">WE HELP YOU EXCEL AT ALL THREE.</p>
    </div>
  </section>

  <section class="card card--contact" aria-label="Card front">
    <div class="contact-brand">
      <span class="brand-square"></span>
      <span class="brand-name">Hollowmere Advisory</span>
    </div>
    <span class="divider"></span>
    <div class="contact-details">
      <h1 class="person-name">DANIEL REYES</h1>
      <p class="person-title">Managing Director</p>
      <ul class="contact-list">
        <li><svg viewBox="0 0 14 14"><rect x="3" y="1" width="8" height="12" rx="1.5" fill="none" stroke="var(--brand-mid)" stroke-width="1.6"/><circle cx="7" cy="10.5" r="0.9" fill="var(--brand-mid)"/></svg>+00 7310 482 615</li>
        <li><svg viewBox="0 0 14 14"><path d="M3 1.5l2.5 0 1 3-1.6 1.2a7 7 0 0 0 3.4 3.4L9.5 7.5l3 1v2.5c0 .8-.7 1.5-1.5 1.5C6 12.5 1.5 8 1.5 3c0-.8.7-1.5 1.5-1.5z" fill="var(--brand-mid)"/></svg>+00 2094 617 208</li>
        <li><svg viewBox="0 0 14 14"><rect x="1.5" y="3" width="11" height="8" rx="1" fill="none" stroke="var(--brand-mid)" stroke-width="1.5"/><path d="M1.8 3.5L7 7.5l5.2-4" fill="none" stroke="var(--brand-mid)" stroke-width="1.5"/></svg>person@HollowmereAdvisory.com</li>
      </ul>
    </div>
    <div class="tagline-band"></div>
    <p class="tagline-pill">Optimize Your Investment in Talent</p>
  </section>
</body>
</html>
```